Vitoplume.com

I need a web design for a Online Wellness Center based in Chicago, IL and it's called "Vitoplume" We provide Health risk assessment to individuals and interventions. Our portal has a Health Activity tracker where our members record health activities and aerobic miles and biometric data. Our Online wellness center tracks the participant's progress toward health goals and awards points for completed activities.
I started working on this website but the designer was not able to designer a website which describes what we do. I need a fresh look on this project. I need a very attractive, responsive website which says what we do.
These are the things we do.
1. We provide Health Risk Assessments to individuals and Co-operations
2. We Provide Free health screenings to undeserved communities
3. Assist individuals access free or affordable medications
4. We ask providers/doctors to see (or do a complete physical) one individual free of charge once a year (those individuals who are no insured and don't have money to pay from their pocket)
5. Assist patient access lab work at low cost
Our goal is to provide services that will lower the cost of care for our members.

Here is the website: www.vitoplume.com still underdevelopment. PLEASE DO NOT COPY THIS STYLE OF WEBSITE. IT'S A BAD DESIGN AND THAT IS WHY I'M RE-DESIGNING THE SITE

Target Market(s)

Health individuals between the age of 21 to 65 Plus years old. Insured and uninsured

Industry/Entity Type

Health And Wellness

Coding

Coded - Design and coding required

Number of Pages Required

5+ page

Colors
0292cd

Requirements
Must have
• I'm still working on this websiteHere is the menu: Home, About us, Services, Health Screening, Providers, Contacts
• Please see. www.vitoplume.com
Nice to have
• Event calender
• Upcoming Event
• Medication
• Lab assist
• Providers/Free Clinics

```html
<!DOCTYPE html>
<html lang="en">
<head>
<meta charset="utf-8">
<title>Vitoplume – Online Wellness Center</title>
<link href="https://fonts.googleapis.com/css2?family=Open+Sans:wght@400;600;700;800&family=Oswald:wght@400;500;600&display=swap" rel="stylesheet">
<style>
:root{
  --blue:#0292cd;
  --navy:#1d3f86;
  --navy-deep:#142e66;
  --green:#7ab83a;
  --green-dark:#5f9a26;
  --footer:#6aac2c;
  --ink:#333;
  --muted:#666;
  --grey:#8a8a8a;
  --light:#f2f2f2;
  --white:#fff;
}
*{margin:0;padding:0;box-sizing:border-box}
html,body{width:1200px;height:2700px;overflow:hidden;background:var(--white)}
body{font-family:"Open Sans",Arial,sans-serif;color:var(--ink);position:relative}
.abs{position:absolute}
.photo{position:absolute}

/* header */
.site-header{left:0;top:0;width:1200px;height:72px;background:var(--white)}
.brand{position:absolute;left:100px;top:18px;display:flex;align-items:center;gap:10px}
.brand-dot{width:30px;height:30px;border-radius:50%;background:var(--green)}
.brand-name{font-size:26px;font-weight:700;color:var(--green)}
.social-top{position:absolute;right:90px;top:22px;display:flex;gap:8px}
.social-top span{width:26px;height:26px;border-radius:50%;background:#555}

/* hero */
.hero{left:0;top:72px;width:1200px;height:528px;background:linear-gradient(90deg,#2b2b2b 0%,#4a4a4a 45%,#7c7c7c 70%,#5a5a5a 100%)}
.hero-copy{position:absolute;left:100px;top:66px;width:640px;color:var(--white)}
.hero-title{font-family:"Oswald",Arial,sans-serif;font-weight:500;font-size:74px;line-height:80px}
.hero-sub{font-family:"Oswald",Arial,sans-serif;font-weight:500;font-size:34px;margin-top:6px;letter-spacing:.5px}
.hero-text{font-size:12px;line-height:17px;width:440px;margin-top:18px;color:#e6e6e6}
.btn{display:inline-block;background:var(--green);color:var(--white);font-weight:600;border-radius:3px}
.hero .btn{font-size:20px;padding:12px 22px;margin-top:42px}
.arrow{position:absolute;top:232px;width:34px;height:52px;background:rgba(255,255,255,.85)}
.arrow svg{width:34px;height:52px}
.arrow.left{left:0}
.arrow.right{right:0}
.dots{position:absolute;left:570px;bottom:14px;display:flex;gap:8px}
.dots span{width:10px;height:10px;border-radius:50%;background:rgba(255,255,255,.5)}
.dots span:first-child{background:var(--white)}

/* nav */
.main-nav{left:0;top:600px;width:1200px;height:32px;background:var(--navy);display:flex;align-items:center;padding-left:100px}
.main-nav a{color:var(--white);font-size:13px;font-weight:600;text-decoration:none;width:166px;text-align:center}
.main-nav a:first-child{width:90px;text-align:left}

/* wellness */
.wellness{left:100px;top:648px;width:630px}
.section-head{font-size:26px;font-weight:600;color:#444;letter-spacing:.3px}
.wellness p{font-size:12px;line-height:17px;color:var(--muted);margin-top:8px}
.wellness .section-head.second{margin-top:18px}
.wellness ul{list-style:none;margin-top:10px}
.wellness li{font-size:12px;line-height:17px;color:var(--muted)}
.wellness li::before{content:"– "}

/* grid */
.services-panel{left:940px;top:972px;width:260px;height:210px;background:var(--navy)}
.services-panel div{color:var(--white);font-size:16px;font-weight:600;padding:12px 20px;border-bottom:1px solid rgba(255,255,255,.15)}
.services-panel div.active{background:var(--green)}
.grid-caption{left:108px;top:1300px;width:640px;height:100px;background:rgba(20,46,102,.75);padding:14px 22px;color:var(--white);font-size:11px;line-height:16px}
.grid-caption .btn{font-size:15px;padding:7px 16px;margin-top:10px}

/* features */
.feature{position:absolute;top:1420px;width:300px;text-align:center}
.feature svg{display:block;margin:0 auto}
.feature h3{font-size:20px;font-weight:700;color:#444;margin-top:12px;line-height:24px}

/* event */
.event-title{left:100px;top:1700px;font-family:"Oswald",Arial,sans-serif;font-weight:500;font-size:58px;line-height:64px;color:#444}
.event-box{left:240px;top:1840px;width:320px;height:190px;background:var(--navy-deep);padding:22px 22px;color:var(--white);font-size:12px;line-height:17px}
.event-box .btn{font-size:16px;padding:8px 14px;margin-top:14px}

/* clinics */
.clinics{left:0;top:2140px;width:1200px;text-align:center}
.clinics h2{font-size:50px;line-height:62px;font-weight:700;color:#333}
.clinics p{width:1020px;margin:6px auto 0;font-size:16px;line-height:23px;color:var(--muted)}
.subscribe{display:flex;justify-content:center;margin-top:14px;height:44px}
.subscribe .field{display:block;width:400px;height:44px;border:1px solid #bbb;background:#fafafa;font-size:16px;line-height:20px;color:#999;padding:11px 16px;text-align:left}
.subscribe .btn{display:block;height:44px;width:130px;font-size:17px;line-height:24px;padding:10px 0;border-radius:0;text-align:center}

/* footer */
.site-footer{left:0;top:2338px;width:1200px;height:362px;background:var(--footer);color:var(--white)}
.footer-brand{position:absolute;left:100px;top:30px;display:flex;align-items:center;gap:10px}
.footer-brand .brand-dot{background:var(--white)}
.footer-brand .brand-name{color:var(--white)}
.footer-tag{position:absolute;left:140px;top:66px;font-size:11px}
.footer-address{position:absolute;left:100px;top:150px;font-size:12px;line-height:18px}
.contact-form{position:absolute;left:470px;top:26px;width:330px}
.form-row{display:flex;align-items:center;margin-bottom:8px}
.form-row label{width:80px;font-size:12px}
.form-row span{flex:1;height:22px;background:var(--white)}
.form-row.msg{align-items:flex-start}
.form-row.msg span{height:80px}
.form-send{margin-left:230px;display:inline-block;background:var(--white);color:var(--green-dark);font-size:11px;font-weight:700;padding:3px 14px}
.follow{position:absolute;left:880px;top:26px;width:240px;text-align:center}
.follow h4{font-size:18px;font-weight:600;letter-spacing:.5px}
.follow span{display:block;width:26px;height:26px;border-radius:50%;background:rgba(255,255,255,.85);margin:14px auto 0}
.copyright{position:absolute;left:0;bottom:0;width:1200px;height:30px;background:var(--green-dark);font-size:11px;padding:8px 100px}
</style>
</head>
<body>

<header class="abs site-header">
  <div class="brand"><span class="brand-dot"></span><span class="brand-name">Vitoplume</span></div>
  <div class="social-top"><span></span><span></span><span></span></div>
</header>

<section class="abs hero">
  <div class="photo" role="img" aria-label="Photograph of a thoughtful woman against a dark backdrop" style="left:700px;top:0;width:500px;height:528px;background:linear-gradient(90deg,rgba(0,0,0,0),rgba(150,150,150,.35) 50%,rgba(0,0,0,.2))"></div>
  <div class="hero-copy">
    <h1 class="hero-title">Do You Know about<br>your risk factor?</h1>
    <div class="hero-sub">WE AVAILS HEALTH SCREENING SERVICE</div>
    <p class="hero-text">Lorem ipsum is simply dummy text of the printing and typesetting industry. Lorem ipsum has been the standard dummy text ever since the 1500s, when an unknown printer took a galley.</p>
    <span class="btn">Learn Your Risk &nbsp;›</span>
  </div>
  <div class="arrow left"><svg viewBox="0 0 34 52"><path d="M21 16 L12 26 L21 36" fill="none" stroke="#333" stroke-width="4"/></svg></div>
  <div class="arrow right"><svg viewBox="0 0 34 52"><path d="M13 16 L22 26 L13 36" fill="none" stroke="#333" stroke-width="4"/></svg></div>
  <div class="dots"><span></span><span></span><span></span></div>
</section>

<nav class="abs main-nav">
  <a>HOME</a><a>ABOUT US</a><a>OUR SERVICES</a><a>HEALTH SCREENING</a><a>PROVIDERS</a><a>CONTACT</a>
</nav>

<section class="abs wellness">
  <h2 class="section-head">OUR WELLNESS SERVICES</h2>
  <p>Vitoplume is an online wellness center where members take a health risk assessment, log activities and biometric data, and earn points toward their goals. We also link people with free screenings, affordable medication and low cost lab work to lower their cost of care.</p>
  <h2 class="section-head second">BENEFITS OF OUR WELLNESS SERVICES</h2>
  <p>Our members gain a clear picture of their health and the support they need to act on it, whether they are insured or not.</p>
  <ul>
    <li>Free health screenings</li>
    <li>Health risk assessment</li>
    <li>Affordable medication support</li>
    <li>Low cost lab work access</li>
    <li>Activity and goal tracking</li>
    <li>Yearly free physical with partner providers</li>
  </ul>
</section>
<div class="photo" role="img" aria-label="Photograph of an older couple talking with a doctor" style="left:752px;top:648px;width:448px;height:312px;background:linear-gradient(135deg,#e7e3dd,#c9c2b8 55%,#a8b6c4)"></div>

<div class="photo" role="img" aria-label="Photograph of a pharmacist at a pharmacy counter" style="left:108px;top:972px;width:640px;height:428px;background:linear-gradient(135deg,#dfe6ea,#b8c6cc 50%,#8fa4ac)"></div>
<div class="abs grid-caption">Lorem ipsum is simply dummy text of the printing industry, used here to describe our medication access service.<br><span class="btn">Read More</span></div>
<div class="photo" role="img" aria-label="Photograph of a laboratory with test tubes" style="left:760px;top:972px;width:180px;height:210px;background:linear-gradient(135deg,#cfe4f2,#7fb3d6 60%,#5a8eb6)"></div>
<div class="abs services-panel">
  <div class="active">MEDICATION ›</div>
  <div>HEALTH SCREENING</div>
  <div>Lab Test</div>
  <div>Wellness Products</div>
</div>
<div class="photo" role="img" aria-label="Photograph of a blood pressure check" style="left:760px;top:1190px;width:250px;height:210px;background:linear-gradient(135deg,#9fb5c8,#5f7f9d)"></div>
<div class="photo" role="img" aria-label="Photograph of medication pills" style="left:1018px;top:1190px;width:182px;height:210px;background:linear-gradient(135deg,#ead9c4,#c79f74)"></div>

<div class="feature" style="left:70px">
  <svg width="110" height="120" viewBox="0 0 110 120"><polygon points="55,4 104,32 104,88 55,116 6,88 6,32" fill="#1d3f86"/><circle cx="55" cy="46" r="12" fill="#fff"/><path d="M33 86 Q55 54 77 86 Z" fill="#fff"/></svg>
  <h3>WHY INDIVISUAL<br>PURSUE IT?</h3>
  <svg width="30" height="14" viewBox="0 0 30 14"><path d="M4 3 L15 11 L26 3" fill="none" stroke="#444" stroke-width="2"/></svg>
</div>
<div class="feature" style="left:450px">
  <svg width="110" height="120" viewBox="0 0 110 120"><polygon points="55,4 104,32 104,88 55,116 6,88 6,32" fill="#1d3f86"/><circle cx="55" cy="42" r="9" fill="#fff"/><circle cx="34" cy="52" r="7" fill="#fff"/><circle cx="76" cy="52" r="7" fill="#fff"/><path d="M40 84 Q55 56 70 84 Z" fill="#fff"/><path d="M22 86 Q34 64 46 86 Z" fill="#fff"/><path d="M64 86 Q76 64 88 86 Z" fill="#fff"/></svg>
  <h3>WHY EMPLOYER<br>PURSUE IT?</h3>
  <svg width="30" height="14" viewBox="0 0 30 14"><path d="M4 3 L15 11 L26 3" fill="none" stroke="#444" stroke-width="2"/></svg>
</div>
<div class="feature" style="left:880px">
  <svg width="110" height="120" viewBox="0 0 110 120"><polygon points="55,4 104,32 104,88 55,116 6,88 6,32" fill="#1d3f86"/><path d="M55 34 L55 66 M55 34 L44 46 M55 34 L66 46" stroke="#fff" stroke-width="6" fill="none"/><rect x="36" y="74" width="38" height="8" fill="#fff"/></svg>
  <h3>OUR WELLNESS<br>PROCESS?</h3>
  <svg width="30" height="14" viewBox="0 0 30 14"><path d="M4 3 L15 11 L26 3" fill="none" stroke="#444" stroke-width="2"/></svg>
</div>

<h2 class="abs event-title">UPCOMING<br>EVENT</h2>
<div class="photo" role="img" aria-label="Photograph of an audience at a health conference" style="left:560px;top:1708px;width:640px;height:412px;background:linear-gradient(160deg,#d8c6a4,#a98a5e 45%,#6b5640)"></div>
<div class="abs event-box">
  Join our free community health screening day in Chicago. Meet local providers, check your blood pressure and sugar levels, and learn how our wellness program can help you reach your goals.<br>
  <span class="btn">Event Calender</span>
</div>

<section class="abs clinics">
  <h2>Free Clinics</h2>
  <p>Lorem Ipsum is simply dummy text of the printing and typesetting industry. Lorem Ipsum has been the industry's standard dummy text ever since the 1500s, when an unknown printer took a galley of type to make a specimen book.</p>
  <div class="subscribe"><span class="field">Enter your Email address</span><span class="btn">Notify me</span></div>
</section>

<footer class="abs site-footer">
  <div class="footer-brand"><span class="brand-dot"></span><span class="brand-name">Vitoplume</span></div>
  <div class="footer-tag">your online wellness center</div>
  <div class="footer-address">VITOPLUME<br>2140 W Larkmoor Ave<br>Chicago, IL 60612<br>(312) 555-0148<br>hello@vitoplume.com<br>www.vitoplume.com</div>
  <div class="contact-form">
    <div class="form-row"><label>Name</label><span></span></div>
    <div class="form-row"><label>Email</label><span></span></div>
    <div class="form-row"><label>Website</label><span></span></div>
    <div class="form-row"><label>Telephone</label><span></span></div>
    <div class="form-row msg"><label>Message</label><span></span></div>
    <span class="form-send">Send</span>
  </div>
  <div class="follow">
    <h4>ALSO FOLLOW US</h4>
    <span></span><span></span><span></span><span></span>
  </div>
  <div class="copyright">© 2015 Vitoplume. All rights reserved.</div>
</footer>

</body>
</html>
```